project - Plume Den

Dear designers, I'm Looking for an appealing new business card design to represent us for our new e-cigarette store: The PlumE Den. Knowledgeable and friendly staff we aim for superior customer service with a positive atmosphere. Classic feel with modern touch is what we are aiming for . Lime green font and grey back round is the original color scheme but we are flexible and open to suggestions. I added some doodles to show you where my mind is at. address: 4826 97 St SW Edmonton, AB (inside the grand bazaar hall)web: theplumeden.com email: info@theplumeden.com phone : 780.555.6147 Thanks and am looking forward to seeing your creative , fresh and innovative designs.
Good luck everybody!
Gavin
lime green and charcoal grey please. thanks
Business
The PlumE Den

```html
<!DOCTYPE html>
<html lang="en">
<head>
<meta charset="utf-8">
<title>The PlumE Den – Business Card</title>
<link href="https://fonts.googleapis.com/css2?family=Mulish:wght@500;600;800&display=swap" rel="stylesheet">
<style>
  :root {
    --page: #e9eaeb;
    --card-top: #f7f7f5;
    --card-bottom: #e6e5e1;
    --lime: #3fae45;
    --charcoal: #4a4a4c;
    --ink: #2f2f31;
    --rule: #8e8f92;
  }
  * { margin: 0; padding: 0; box-sizing: border-box; }
  html, body {
    width: 1200px; height: 768px; overflow: hidden;
    background: var(--page);
    font-family: "Mulish", sans-serif;
  }
  .card {
    position: absolute; left: 160px; top: 129px;
    width: 880px; height: 510px;
    border-radius: 24px; overflow: hidden;
    background: linear-gradient(160deg, var(--card-top), var(--card-bottom));
    box-shadow: 0 10px 30px rgba(0,0,0,.12);
  }
  .brand {
    position: absolute; right: 64px; top: 80px;
    text-align: right; color: var(--lime);
    font-weight: 800; font-size: 80px; line-height: 78px;
    letter-spacing: -1px;
  }
  .person { position: absolute; left: 37px; top: 160px; }
  .person__name {
    color: var(--ink); font-weight: 600; font-size: 24px;
    letter-spacing: 2px; text-transform: uppercase;
  }
  .person__role {
    margin-top: 12px; color: var(--lime);
    font-weight: 600; font-size: 20px; letter-spacing: .5px;
  }
  .divider {
    position: absolute; left: 53px; top: 252px;
    width: 763px; height: 2px;
    background: var(--rule); opacity: .5;
  }
  .address {
    position: absolute; left: 37px; top: 330px;
    color: var(--ink); font-weight: 500; font-size: 20px;
    line-height: 30px; letter-spacing: 1px;
  }
  .contacts {
    position: absolute; right: 36px; top: 268px;
    list-style: none; text-align: right; color: var(--ink);
  }
  .contacts li {
    display: flex; justify-content: flex-end; align-items: center;
    gap: 12px; height: 42px;
    font-weight: 500; font-size: 18px; letter-spacing: 1.5px;
  }
  .contacts li.contacts__small { height: 31px; font-size: 16px; letter-spacing: .5px; }
  .contacts svg { width: 20px; height: 20px; fill: var(--charcoal); flex: none; }
  .footer-band {
    position: absolute; left: 0; bottom: 0;
    width: 880px; height: 40px;
    background: var(--lime);
    display: flex; align-items: center; padding-left: 37px;
  }
  .footer-web {
    color: #fff; font-weight: 600; font-size: 16px; letter-spacing: .5px;
  }
</style>
</head>
<body>
  <main class="card">
    <div class="brand">PLUME<br>DEN</div>

    <div class="person">
      <p class="person__name">Owen Castell</p>
      <p class="person__role">Managing Director</p>
    </div>

    <div class="divider"></div>

    <p class="address">4826 97 St SW<br>Grand Bazaar Hall</p>

    <ul class="contacts">
      <li>780.555.6147
        <svg viewBox="0 0 24 24" aria-hidden="true"><path d="M6.6 10.8a15.1 15.1 0 0 0 6.6 6.6l2.2-2.2c.3-.3.7-.4 1-.2 1.1.4 2.3.6 3.6.6.6 0 1 .4 1 1V20c0 .6-.4 1-1 1A17 17 0 0 1 3 4c0-.6.4-1 1-1h3.5c.6 0 1 .4 1 1 0 1.3.2 2.5.6 3.6.1.3 0 .7-.2 1z"/></svg>
      </li>
      <li>780.555.6148
        <svg viewBox="0 0 24 24" aria-hidden="true"><path d="M7 1h10a2 2 0 0 1 2 2v18a2 2 0 0 1-2 2H7a2 2 0 0 1-2-2V3a2 2 0 0 1 2-2zm0 3v15h10V4zm5 16.2a1 1 0 1 0 0 .1z"/></svg>
      </li>
      <li>780.555.6149
        <svg viewBox="0 0 24 24" aria-hidden="true"><path d="M3 8h3V2h10l3 3v3h2v14H3zm5-4v4h9V6h-2V4zm-3 6v10h14V10zm2 2h4v2H7zm0 3h4v2H7zm6-3h4v6h-4z"/></svg>
      </li>
      <li class="contacts__small">info@theplumeden.com
        <svg viewBox="0 0 24 24" aria-hidden="true"><path d="M2 5h20v14H2zm2 2v.3l8 5.5 8-5.5V7zm0 2.7V17h16V9.7l-8 5.5z"/></svg>
      </li>
      <li class="contacts__small">www.theplumeden.com
        <svg viewBox="0 0 24 24" aria-hidden="true"><path d="M12 2a10 10 0 1 0 0 20 10 10 0 0 0 0-20zm6.9 6h-3a15 15 0 0 0-1.3-3.9A8 8 0 0 1 18.9 8zM12 4c.8 1.1 1.5 2.5 1.9 4h-3.8c.4-1.5 1.1-2.9 1.9-4zM4.3 14a8 8 0 0 1 0-4h3.4a16 16 0 0 0 0 4zm.8 2h3a15 15 0 0 0 1.3 3.9A8 8 0 0 1 5.1 16zm3-8h-3a8 8 0 0 1 4.3-3.9C8.8 5.3 8.4 6.6 8.1 8zM12 20c-.8-1.1-1.5-2.5-1.9-4h3.8c-.4 1.5-1.1 2.9-1.9 4zm2.3-6H9.7a14 14 0 0 1 0-4h4.6a14 14 0 0 1 0 4zm.3 5.9c.6-1.2 1-2.5 1.3-3.9h3a8 8 0 0 1-4.3 3.9zm1.7-5.9a16 16 0 0 0 0-4h3.4a8 8 0 0 1 0 4z"/></svg>
      </li>
    </ul>

    <div class="footer-band">
      <p class="footer-web">www.theplumeden.com</p>
    </div>
  </main>
</body>
</html>
```